Harbor Nightclub

Nightclub flyer., digital single sided, for KV and PX. I included samples of some previous flyers we've used. Sample Info:
HARBOR
FRIDAYS
FRI MAY 1 2020
DJ VORTAN (club floor)
DJ RUZO & DJ TAV (residents on the lounge floor)
4217 Marlow Avenue Sacramento
www.harborvenuehall.example for list/VIP inquiries

Target Market(s)

Upscale top 40 crowd but want some cool and artsy like the examples included.

Font styles to use
Sans Serif

Requirements
Must have
• Harbor Logo
Nice to have
• Would be nice if the flyer can be incorporated later with DJ photos (sometimes we will add dj photos to pixagram etc). Would like a big city type of feel.
Should not have
• Nothing too sexual.

```html
<!DOCTYPE html>
<html lang="en">
<head>
<meta charset="utf-8">
<title>Harbor Fridays</title>
<link rel="stylesheet" href="https://fonts.googleapis.com/css2?family=Syncopate:wght@400;700&display=swap">
<style>
  :root {
    --night: #2a1f5e;
    --night-deep: #221a4f;
    --violet: #4a2f9a;
    --magenta: #d4195e;
    --ring: #c81a5a;
    --red: #e8262c;
    --amber: #e0962a;
    --cyan: #39b6d8;
    --white: #ffffff;
    --head: "Syncopate", "Century Gothic", sans-serif;
  }
  * { margin: 0; padding: 0; box-sizing: border-box; }
  html, body { overflow: hidden; background: var(--night-deep); }
  .flyer {
    position: relative;
    width: 846px;
    height: 1200px;
    overflow: hidden;
    background: var(--night);
    font-family: var(--head);
    color: var(--white);
  }
  .street-scene {
    position: absolute; inset: 0;
    background:
      radial-gradient(ellipse at 75% 35%, rgba(80,110,255,0.35), transparent 55%),
      radial-gradient(ellipse at 35% 70%, rgba(200,40,110,0.35), transparent 60%),
      linear-gradient(180deg, #3a2a86 0%, #3b2478 45%, #2b1f5d 75%, #241a50 100%);
  }
  .shapes { position: absolute; inset: 0; }
  .text {
    position: absolute; left: 0; width: 846px; margin: 0;
    text-align: center; white-space: nowrap; line-height: 1;
  }
  .title {
    top: 146px; font-size: 96px; font-weight: 700; letter-spacing: 4px;
    text-shadow: 2px -2px 0 rgba(232,38,44,0.8);
  }
  .subtitle { top: 268px; font-size: 32px; font-weight: 400; letter-spacing: 26px; padding-left: 26px; }
  .dj-name {
    position: absolute; width: 260px; margin: 0; line-height: 1;
    text-align: center; white-space: nowrap; font-size: 20px; font-weight: 700; letter-spacing: 1px;
  }
  .dj-floor {
    position: absolute; width: 260px; margin: 0; line-height: 1;
    text-align: center; white-space: nowrap; font-size: 10px; letter-spacing: 7px; padding-left: 7px;
  }
  .headliner-name { left: 293px; top: 640px; }
  .headliner-floor { left: 293px; top: 668px; }
  .resident-left-name { left: 42px; top: 776px; }
  .resident-left-floor { left: 42px; top: 805px; }
  .resident-right-name { left: 542px; top: 776px; }
  .resident-right-floor { left: 542px; top: 805px; }
  .wordmark { top: 864px; font-size: 44px; font-weight: 400; letter-spacing: 2px; }
  .date { top: 960px; font-size: 25px; font-weight: 700; letter-spacing: 12px; padding-left: 12px; }
  .address { top: 1002px; font-size: 18px; font-weight: 700; letter-spacing: 6px; padding-left: 6px; }
  .inquiries { top: 1088px; font-size: 13px; letter-spacing: 5px; padding-left: 5px; }
  .website { top: 1111px; font-size: 18px; letter-spacing: 3px; padding-left: 3px; }
</style>
</head>
<body>
<main class="flyer">
  <div class="street-scene" role="img" aria-label="Night street scene with a crowd outside the club, tinted purple and magenta"></div>

  <svg class="shapes" width="846" height="1200" viewBox="0 0 846 1200">
    <defs>
      <linearGradient id="ring-fade" x1="0" y1="0" x2="0" y2="1">
        <stop offset="0" stop-color="#c81a5a" stop-opacity="0.95"/>
        <stop offset="1" stop-color="#c81a5a" stop-opacity="0.35"/>
      </linearGradient>
      <linearGradient id="band-amber" x1="0" x2="1">
        <stop offset="0" stop-color="#e0962a" stop-opacity="0.8"/>
        <stop offset="1" stop-color="#d4195e" stop-opacity="0.25"/>
      </linearGradient>
      <linearGradient id="band-cyan" x1="0" x2="1">
        <stop offset="0" stop-color="#39b6d8"/>
        <stop offset="1" stop-color="#39b6d8" stop-opacity="0"/>
      </linearGradient>
      <linearGradient id="band-red" x1="0" x2="1">
        <stop offset="0" stop-color="#e8262c"/>
        <stop offset="1" stop-color="#e8262c" stop-opacity="0.5"/>
      </linearGradient>
      <linearGradient id="portrait-tone" x1="0" y1="0" x2="0" y2="1">
        <stop offset="0" stop-color="#6f74e8"/>
        <stop offset="1" stop-color="#3a2b95"/>
      </linearGradient>
      <linearGradient id="portrait-light" x1="0" y1="0" x2="0" y2="1">
        <stop offset="0" stop-color="#f1eefc"/>
        <stop offset="1" stop-color="#8d7fd8"/>
      </linearGradient>
      <linearGradient id="mascot-tone" x1="0" y1="0" x2="0" y2="1">
        <stop offset="0" stop-color="#a9b6f8"/>
        <stop offset="1" stop-color="#d8506f"/>
      </linearGradient>
    </defs>

    <!-- ring -->
    <circle cx="423" cy="376" r="287" fill="none" stroke="url(#ring-fade)" stroke-width="52"/>

    <!-- accent bands -->
    <rect x="581" y="47" width="35" height="7" fill="#e8262c" opacity="0.8"/>
    <rect x="581" y="75" width="120" height="8" fill="url(#band-cyan)" opacity="0.7"/>
    <rect x="647" y="103" width="199" height="24" fill="url(#band-red)" opacity="0.85"/>
    <rect x="616" y="141" width="199" height="57" fill="url(#band-amber)" opacity="0.6"/>
    <rect x="0" y="713" width="157" height="57" fill="url(#band-cyan)" opacity="0.8"/>
    <rect x="28" y="788" width="76" height="13" fill="#e0962a" opacity="0.8"/>
    <rect x="28" y="812" width="230" height="3" fill="#e8262c"/>
    <rect x="68" y="826" width="200" height="3" fill="#e0962a" opacity="0.8"/>
    <rect x="692" y="1118" width="60" height="6" fill="#e8262c" opacity="0.9"/>
    <rect x="692" y="1130" width="154" height="2" fill="#e8262c" opacity="0.5"/>

    <!-- level bars left -->
    <g fill="#d4195e">
      <rect x="25" y="830" width="31" height="10" opacity="0.3"/>
      <rect x="25" y="854" width="31" height="10" opacity="0.35"/>
      <rect x="25" y="879" width="31" height="10" opacity="0.4"/>
      <rect x="25" y="903" width="31" height="10" opacity="0.45"/>
      <rect x="25" y="928" width="31" height="10" opacity="0.5"/>
      <rect x="25" y="952" width="31" height="10" opacity="0.55"/>
      <rect x="25" y="977" width="31" height="10" opacity="0.6"/>
      <rect x="25" y="1001" width="31" height="10" opacity="0.65"/>
      <rect x="25" y="1026" width="31" height="10" opacity="0.7"/>
      <rect x="25" y="1050" width="31" height="10" opacity="0.75"/>
      <rect x="25" y="1075" width="31" height="10" opacity="0.8"/>
      <rect x="25" y="1099" width="31" height="10" opacity="0.85"/>
      <rect x="25" y="1124" width="31" height="10" opacity="0.9"/>
    </g>
    <!-- level bars right -->
    <g fill="#d4195e">
      <rect x="784" y="621" width="32" height="10" opacity="0.2"/>
      <rect x="784" y="645" width="32" height="10" opacity="0.25"/>
      <rect x="784" y="670" width="32" height="10" opacity="0.3"/>
      <rect x="784" y="694" width="32" height="10" opacity="0.35"/>
      <rect x="784" y="719" width="32" height="10" opacity="0.4"/>
      <rect x="784" y="743" width="32" height="10" opacity="0.45"/>
      <rect x="784" y="768" width="32" height="10" opacity="0.5"/>
      <rect x="784" y="792" width="32" height="10" opacity="0.55"/>
      <rect x="784" y="817" width="32" height="10" opacity="0.6"/>
      <rect x="784" y="841" width="32" height="10" opacity="0.65"/>
      <rect x="784" y="866" width="32" height="10" opacity="0.7"/>
      <rect x="784" y="890" width="32" height="10" opacity="0.75"/>
      <rect x="784" y="915" width="32" height="10" opacity="0.8"/>
      <rect x="784" y="939" width="32" height="10" opacity="0.85"/>
      <rect x="784" y="964" width="32" height="10" opacity="0.9"/>
      <rect x="784" y="988" width="32" height="10" opacity="0.95"/>
      <rect x="784" y="1013" width="32" height="10"/>
      <rect x="732" y="841" width="32" height="10" opacity="0.2"/>
      <rect x="732" y="890" width="32" height="10" opacity="0.25"/>
      <rect x="732" y="939" width="32" height="10" opacity="0.3"/>
      <rect x="732" y="988" width="32" height="10" opacity="0.35"/>
      <rect x="732" y="1037" width="32" height="10" opacity="0.4"/>
    </g>

    <!-- DJ portrait frames -->
    <g class="dj-frame headliner">
      <polygon points="423,382 525,441 525,558 423,617 321,558 321,441" fill="none" stroke="#e8262c" stroke-width="1.5"/>
      <polygon points="423,392 514,445 514,553 423,606 332,553 332,445" fill="url(#portrait-tone)" role="img" aria-label="Portrait photo of DJ Vortan"/>
    </g>
    <g class="dj-frame resident-left">
      <polygon points="172,518 274,577 274,694 172,753 70,694 70,577" fill="none" stroke="#e8262c" stroke-width="1.5"/>
      <polygon points="172,528 263,581 263,689 172,742 81,689 81,581" fill="url(#portrait-light)" role="img" aria-label="Portrait photo of DJ Ruzo"/>
    </g>
    <g class="dj-frame resident-right">
      <polygon points="672,518 774,577 774,694 672,753 570,694 570,577" fill="none" stroke="#e8262c" stroke-width="1.5"/>
      <polygon points="672,528 763,581 763,689 672,742 581,689 581,581" fill="url(#mascot-tone)" role="img" aria-label="Mascot illustration for DJ Tav"/>
    </g>

    <!-- brand mark circle -->
    <circle cx="423" cy="776" r="58" fill="none" stroke="#ffffff" stroke-width="6"/>
  </svg>

  <h1 class="text title">HARBOR</h1>
  <p class="text subtitle">FRIDAYS</p>

  <p class="dj-name headliner-name">DJ VORTAN</p>
  <p class="dj-floor headliner-floor">CLUB FLOOR</p>
  <p class="dj-name resident-left-name">DJ RUZO</p>
  <p class="dj-floor resident-left-floor">LOUNGE FLOOR</p>
  <p class="dj-name resident-right-name">DJ TAV</p>
  <p class="dj-floor resident-right-floor">LOUNGE FLOOR</p>

  <p class="text wordmark">HARBOR</p>

  <p class="text date">FRI | MAY 1 2020</p>
  <p class="text address">4217 MARLOW AVENUE SACRAMENTO</p>

  <p class="text inquiries">FOR LIST/VIP INQUIRIES</p>
  <p class="text website">WWW.HARBORVENUEHALL.EXAMPLE</p>
</main>
</body>
</html>
```